Business Card Design - Photographer

I am a landscape photographer and I require a business card design. 

I require two designs:
1)  a double sided business card
 and
b)  a single sided business card 

The single sided design can either be the same as the double sided (with just one side having all the information)....or it can be an entire new design. Its up to you.

My corporate colours are (CMYK):

Blue   69, 32, 0, 0
Grey  72,  64,  47,  31
Green  32,  2,  91,  0
Yellow   0, 19, 92, 0
Orange  0, 39, 75, 0

Colour space in final file should be in CMYK.

The details that need to be included on the card:

- Use the provided Logo
- Name: Lukas Wendrovski
- Email:   sales@vistaplume.com.au
- Website:    vistaplume.com.au
- Twitter:    twitter.com/vistaplume
- Facebook:   facebook.com/vistaplume
- Mobile  0415 309 662

Please use the attached template to design the logo to the specified size, including the marked bleed lines. I have also attached my logo in PNG (transparent background) and ai format for you to use.

The final file should be:
- Photoshop version with layers so I can edit the name/text etc. All non vector files should be high resolution at 1039 x 697 pixels at 300 dpi.

I also require a file as:
- Vector based PDF

Anyway questions please contact me.

Thank you

Industry/Entity Type

Landscape

Logo styles of interest
Pictorial/Combination Logo
Abstract Logo
Wordmark Logo
Lettermark Logo
Requirements
Must have
• The details that need to be included on the card:

- Use the provided Logo
- Name: Lukas Wendrovski
- Email: sales@vistaplume.com.au
- Website: vistaplume.com.au
- Twitter: twitter.com/vistaplume
- Facebook: facebook.com/vistaplume
- Mobile 0415 309 662

```html
<!DOCTYPE html>
<html lang="en">
<head>
<meta charset="utf-8">
<title>Vista Plume — Business Card</title>
<link href="https://fonts.googleapis.com/css2?family=Cinzel:wght@500&family=Source+Sans+3:wght@400&display=swap" rel="stylesheet">
<style>
  :root {
    --stage: #3b3b3d;
    --slate: #41414f;
    --paper: #ffffff;
    --ink: #41414f;
    --ink-soft: #55555f;
    --rule: #5a5a66;
    --ghost-dark: rgba(255,255,255,0.12);
    --ghost-light: rgba(65,65,79,0.06);
    --leaf-dark: rgba(255,255,255,0.05);
    --leaf-light: rgba(240,200,120,0.12);
  }
  * { box-sizing: border-box; margin: 0; padding: 0; }
  html, body { width: 1200px; height: 900px; overflow: hidden; background: var(--stage); }
  .stage { position: relative; width: 1200px; height: 900px; }

  .card {
    position: absolute; top: 308px; width: 513px; height: 283px;
    border-radius: 16px; overflow: hidden;
  }
  .card--front { left: 73px; background: var(--slate); }
  .card--back { left: 616px; background: var(--paper); }

  .foliage { position: absolute; border-radius: 40%; }
  .card--front .foliage { left: 0; top: 37px; width: 115px; height: 190px; background: var(--leaf-dark); }
  .card--back .foliage {
    left: 0; top: 50px; width: 120px; height: 185px;
    background: linear-gradient(160deg, rgba(74,146,208,0.10), var(--leaf-light));
  }

  .ghost-ring {
    position: absolute; left: 395px; top: 33px; width: 230px; height: 230px;
    border-radius: 50%; border: 1px solid var(--ghost-dark);
  }
  .ghost-disc {
    position: absolute; left: 420px; top: 28px; width: 210px; height: 210px;
    border-radius: 50%; background: var(--ghost-light);
  }

  .brand { position: absolute; text-align: center; }
  .card--front .brand { left: 0; width: 513px; top: 65px; }
  .card--back .brand { left: 22px; width: 240px; top: 75px; }
  .brand__dot { display: block; margin: 0 auto; border-radius: 50%; background: var(--paper); }
  .card--front .brand__dot { width: 92px; height: 92px; }
  .card--back .brand__dot { width: 84px; height: 84px; background: var(--ink); }
  .brand__name {
    display: block; font-family: "Cinzel", serif; font-weight: 500;
    font-size: 25px; letter-spacing: 0.5px; line-height: 30px;
  }
  .card--front .brand__name { color: var(--paper); margin-top: 14px; }
  .card--back .brand__name { color: var(--ink); margin-top: 8px; }

  .divider {
    position: absolute; left: 274px; top: 75px; width: 1px; height: 133px; background: var(--rule);
  }

  .contact { position: absolute; left: 288px; top: 86px; font-family: "Source Sans 3", sans-serif; color: var(--ink); }
  .contact__name { font-size: 18.5px; letter-spacing: 0.2px; margin-bottom: 4px; }
  .contact__list { list-style: none; }
  .contact__item { display: flex; align-items: center; height: 16.2px; font-size: 12.5px; color: var(--ink-soft); }
  .contact__icon { width: 10px; height: 10px; margin-right: 12px; flex: none; }
  .contact__square { width: 9px; height: 9px; background: var(--ink); margin-right: 13px; border-radius: 1px; flex: none; }
</style>
</head>
<body>
<main class="stage">

  <section class="card card--front" aria-label="Card front">
    <div class="foliage" role="img" aria-label="Faint leaf decoration"></div>
    <div class="ghost-ring"></div>
    <div class="brand">
      <span class="brand__dot"></span>
      <span class="brand__name">VISTA PLUME</span>
    </div>
  </section>

  <section class="card card--back" aria-label="Card back">
    <div class="foliage" role="img" aria-label="Faint coloured leaf decoration"></div>
    <div class="ghost-disc"></div>
    <div class="brand">
      <span class="brand__dot"></span>
      <span class="brand__name">VISTA PLUME</span>
    </div>
    <div class="divider"></div>
    <div class="contact">
      <p class="contact__name">Lukas Wendrovski</p>
      <ul class="contact__list">
        <li class="contact__item">
          <svg class="contact__icon" viewBox="0 0 10 10" fill="none" stroke="#41414f" stroke-width="1"><circle cx="5" cy="5" r="4.3"/><ellipse cx="5" cy="5" rx="1.9" ry="4.3"/><line x1="0.7" y1="5" x2="9.3" y2="5"/></svg>
          vistaplume.com.au
        </li>
        <li class="contact__item"><span class="contact__square"></span>frondly.com/vistaplume</li>
        <li class="contact__item"><span class="contact__square"></span>chirpnet.com/vistaplume</li>
        <li class="contact__item">
          <svg class="contact__icon" viewBox="0 0 10 10"><rect x="0.5" y="2" width="9" height="6.5" fill="#41414f"/><path d="M0.8 2.3 L5 5.6 L9.2 2.3" fill="none" stroke="#fff" stroke-width="0.8"/></svg>
          sales@vistaplume.com.au
        </li>
        <li class="contact__item">
          <svg class="contact__icon" viewBox="0 0 10 10"><rect x="2.5" y="0.5" width="5" height="9" rx="1" fill="#41414f"/><rect x="3.4" y="1.6" width="3.2" height="5" fill="#fff"/></svg>
          0415 309 662
        </li>
      </ul>
    </div>
  </section>

</main>
</body>
</html>
```